Dune Air & Plus business card

I need an awesome, double-sided business card designed with our new logo. I would like the one side black with the colored logo, and the back side is all yours. I'd like to see horizontal and vertical layouts. Get creative! Thank you.

Target Market(s)

HVAC, Heating and Cooling in Phoenix, AZ

Industry/Entity Type

HVAC

Contact Information for Business Card

We need our new logo on the card. Tom Harker, (623) 555-0142, tom@trydunesair.com, www.trydunesair.com, ROC 514273

```html
<!DOCTYPE html>
<html lang="en">
<head>
<meta charset="utf-8">
<title>Dune Air &amp; Plus – Business Card</title>
<link rel="stylesheet" href="https://fonts.googleapis.com/css2?family=Orbitron:wght@800&family=Poppins:wght@500;600;700&display=swap">
<style>
  :root {
    --page: #ffffff;
    --card-black: #141414;
    --card-deep: #050505;
    --band-line: #3a2414;
    --orange: #f07a1a;
    --orange-deep: #e0501a;
    --blue: #1a6fd6;
    --blue-deep: #0f4fae;
    --ink: #1c1c1c;
    --white: #ffffff;
    --panel-soft: #f6f6f6;
  }
  * { margin: 0; padding: 0; box-sizing: border-box; }
  html, body { width: 800px; height: 1200px; overflow: hidden; background: var(--page); }
  .canvas { position: relative; width: 800px; height: 1200px; }

  .card {
    position: absolute; left: 90px; width: 620px; height: 354px;
    overflow: hidden; background: var(--card-black);
    box-shadow: 0 10px 28px rgba(0,0,0,0.22);
  }
  .card-front { top: 190px; }
  .card-back { top: 640px; }
  .card-art { position: absolute; inset: 0; width: 620px; height: 354px; }

  .brand-name {
    position: absolute; font-family: "Poppins", sans-serif; font-weight: 700;
    color: var(--blue); white-space: nowrap; text-align: center; line-height: 1;
  }
  .card-front .brand-name { left: 0; width: 620px; top: 129px; font-size: 42px; }
  .card-back .brand-name { left: 20px; width: 260px; top: 183px; font-size: 27px; }

  .web-pill {
    position: absolute; left: 171px; top: 272px; width: 278px; height: 30px;
    font-family: "Poppins", sans-serif; font-weight: 500; font-size: 14px;
    letter-spacing: 3px; color: var(--white); text-align: center; line-height: 30px;
  }
  .web-pill .domain { color: var(--blue); font-weight: 700; }

  .contact-block { position: absolute; left: 363px; top: 87px; font-family: "Poppins", sans-serif; }
  .person-name {
    font-family: "Orbitron", sans-serif; font-weight: 800; font-size: 23px;
    color: var(--blue-deep); line-height: 1; letter-spacing: 0.3px;
  }
  .person-role { font-size: 11px; font-weight: 600; color: var(--ink); margin-top: 12px; line-height: 1; letter-spacing: 0.2px; }
  .contact-list { list-style: none; margin-top: 16px; }
  .contact-item {
    display: flex; align-items: center; gap: 9px; height: 24px; margin-bottom: 10px;
    font-size: 15px; font-weight: 600; color: var(--ink); white-space: nowrap;
  }
  .contact-icon { width: 22px; height: 24px; flex: none; }
  .license { font-size: 14px; font-weight: 600; color: var(--ink); line-height: 16px; }
  .license-label { color: var(--orange); }
</style>
</head>
<body>
<main class="canvas">

  <section class="card card-front" aria-label="Card front">
    <svg class="card-art" viewBox="0 0 620 354" aria-hidden="true">
      <defs>
        <linearGradient id="bandOrange" x1="0" x2="1">
          <stop offset="0" stop-color="var(--orange-deep)"/>
          <stop offset="1" stop-color="var(--orange)"/>
        </linearGradient>
      </defs>
      <rect width="620" height="354" fill="var(--card-black)"/>
      <polygon points="0,223 0,354 620,354 620,223 310,354" fill="var(--card-deep)"/>
      <polyline points="0,223 232,354" fill="none" stroke="var(--band-line)" stroke-width="1.5"/>
      <polyline points="620,223 388,354" fill="none" stroke="var(--band-line)" stroke-width="1.5"/>
      <rect x="0" y="279" width="620" height="16" fill="url(#bandOrange)"/>
      <rect x="171" y="272" width="278" height="30" rx="15" fill="var(--card-black)"/>
    </svg>
    <p class="brand-name">Dune Air &amp; Plus</p>
    <p class="web-pill">www.<span class="domain">trydunesair</span>.com</p>
  </section>

  <section class="card card-back" aria-label="Card back">
    <svg class="card-art" viewBox="0 0 620 354" aria-hidden="true">
      <defs>
        <linearGradient id="panelSoft" x1="0" y1="0" x2="1" y2="1">
          <stop offset="0" stop-color="var(--white)"/>
          <stop offset="1" stop-color="var(--panel-soft)"/>
        </linearGradient>
      </defs>
      <rect width="620" height="354" fill="var(--card-black)"/>
      <polygon points="340,0 620,0 620,354 336,354 280,177" fill="var(--orange)"/>
      <polygon points="352,0 620,0 620,354 348,354 292,177" fill="url(#panelSoft)"/>
    </svg>

    <p class="brand-name">Dune Air &amp; Plus</p>

    <div class="contact-block">
      <h1 class="person-name">TOM HARKER</h1>
      <p class="person-role">COMPANY MANAGER</p>
      <ul class="contact-list">
        <li class="contact-item">
          <svg class="contact-icon" viewBox="0 0 22 24" aria-hidden="true">
            <polygon points="11,1 21,6.5 21,17.5 11,23 1,17.5 1,6.5" fill="var(--orange)"/>
            <path d="M7.5 7.5c.8-.6 1.6-.4 2 .3l.9 1.6c.3.6.1 1.2-.4 1.5l-.6.4c.5 1.3 1.5 2.3 2.8 2.9l.4-.6c.4-.5 1-.6 1.5-.3l1.6 1c.6.4.8 1.2.2 1.9-.8 1-2.2 1.3-3.6.6-2.4-1.2-4.2-3.2-5.2-5.6-.5-1.3-.4-2.9.4-3.7z" fill="var(--white)"/>
          </svg>
          <span>(623) 555-0142</span>
        </li>
        <li class="contact-item">
          <svg class="contact-icon" viewBox="0 0 22 24" aria-hidden="true">
            <polygon points="11,1 21,6.5 21,17.5 11,23 1,17.5 1,6.5" fill="var(--orange)"/>
            <rect x="5.5" y="8.5" width="11" height="7.5" fill="none" stroke="var(--white)" stroke-width="1.3"/>
            <polyline points="5.5,8.5 11,13 16.5,8.5" fill="none" stroke="var(--white)" stroke-width="1.3"/>
          </svg>
          <span>tom@trydunesair.com</span>
        </li>
        <li class="contact-item">
          <svg class="contact-icon" viewBox="0 0 22 24" aria-hidden="true">
            <polygon points="11,1 21,6.5 21,17.5 11,23 1,17.5 1,6.5" fill="var(--orange)"/>
            <g fill="none" stroke="var(--white)" stroke-width="1.1">
              <circle cx="11" cy="12" r="5.5"/>
              <ellipse cx="11" cy="12" rx="2.4" ry="5.5"/>
              <line x1="5.5" y1="12" x2="16.5" y2="12"/>
            </g>
          </svg>
          <span>www.trydunesair.com</span>
        </li>
      </ul>
      <p class="license"><span class="license-label">ROC</span> 514273</p>
    </div>
  </section>

</main>
</body>
</html>
```